EmberDepot, Charcoal bag packaging and brand

I'm looking at a package design for 10 KG/22 pounds of charcoal.
The design must include a name that is catchy and conveys quality, heat and low ash. The name must not violate any trademarks or tradenames. One of the best resources to view other packaging is the Quiet Pelican website. www.quietpelican.com
Two colors only and one must be red which will be printed on a kraft paper bag. The name EMBERDEPOT.COM must be prominent and also list our website of www.emberdepot.com.
Updates
Here is some wording for the front of the bag and it can be in any order. Make it look GREAT! Use the name "Blazewood Charcoal", but the Emberdepot logo should be the most prominant. Hi Heat, Low Ash, Long burning We will need some wording on the back and sides, but it's primarily just text and we won't worry about it until later. A UPC code will be necessary also. Thanks, Rick Tolben
100% Natural Hardwood Lump Charcoal
Restaurant and Competition grade
No additives, No fillers
Non sparking
Easy lighting, use a chimney starter
Mild flavor profile
A number of the designs are using full coverage ink.
Please limit the amount of ink coverage to no more than 25% ..
It becomes very costly to use 100% coverage.
Thanks!
Rick Tolben
Thank you to all the fine designers.
It was an extremely difficult decision for us. One fine designer was knocked out of the competition by our attorneys and we also received notice from the same attorneys that our brand of "Blazewood Charcoal" won't work...
I'll be posting another new logo design for branding of the charcoal at some point.
Kindest regards to all.
Rick Tolben
Target Market(s)
End users, restaurants, resorts, competition cookoffs
Look and feel
Each slider illustrates characteristics of the customer's brand and the style your logo design should communicate.

```html
<!DOCTYPE html>
<html lang="en">
<head>
<meta charset="utf-8">
<title>EmberDepot – Blazewood Charcoal Bag Front</title>
<link href="https://fonts.googleapis.com/css2?family=Archivo+Black&family=Rye&family=Roboto+Condensed:wght@400;700;800&display=swap" rel="stylesheet">
<style>
  :root {
    --kraft: #d8ab6c;
    --kraft-dark: #c99a5c;
    --ink: #1c1512;
    --red: #e3202b;
    --cream: #fbf1e0;
    --smoke: #8a7154;
  }
  * { margin: 0; padding: 0; box-sizing: border-box; }
  html, body { width: 753px; height: 1200px; overflow: hidden; background: var(--kraft); }
  .bag {
    position: relative; width: 753px; height: 1200px; overflow: hidden;
    background: var(--kraft); color: var(--ink);
    font-family: "Roboto Condensed", "Arial Narrow", sans-serif;
  }
  .bag__top-band {
    position: absolute; left: 0; top: 0; width: 100%; height: 112px;
    background: linear-gradient(180deg, var(--kraft-dark), var(--kraft));
  }
  .brand {
    position: absolute; left: 0; top: 270px; width: 100%; text-align: center;
    font-family: "Archivo Black", sans-serif; font-size: 66px; line-height: 1;
    letter-spacing: 1px; color: var(--ink);
  }
  .rule {
    position: absolute; left: 81px; width: 591px; height: 4px; background: var(--ink);
  }
  .rule::before, .rule::after {
    content: ""; position: absolute; top: -4px; width: 12px; height: 12px;
    border-radius: 50%; background: var(--ink);
  }
  .rule::before { left: -6px; }
  .rule::after { right: -6px; }
  .rule--upper { top: 418px; }
  .rule--lower { top: 678px; }
  .product-name {
    position: absolute; left: 0; width: 100%; text-align: center;
    font-family: "Rye", serif; color: var(--ink);
    text-shadow: 4px 4px 0 var(--red);
  }
  .product-name__first { top: 444px; font-size: 92px; line-height: 1; }
  .product-name__second { top: 566px; font-size: 76px; line-height: 1; }
  .tagline {
    position: absolute; left: 81px; top: 702px; width: 591px; height: 43px;
    background: var(--red); border-radius: 22px; color: var(--cream);
    font-weight: 800; font-size: 27px; line-height: 43px; text-align: center; letter-spacing: .5px;
  }
  .smoke-art {
    position: absolute; left: 610px; top: 672px; width: 143px; height: 368px;
    background: linear-gradient(180deg, rgba(138,113,84,0) 0%, rgba(138,113,84,.55) 40%, rgba(138,113,84,.35) 100%);
    border-radius: 70px 0 0 70px;
  }
  .flame-art {
    position: absolute; left: 427px; top: 855px; width: 326px; height: 345px;
    background: radial-gradient(ellipse at 80% 100%, var(--red) 55%, rgba(227,32,43,.85) 70%, rgba(227,32,43,0) 100%);
  }
  .features { position: absolute; left: 81px; top: 776px; }
  .feature__head {
    font-weight: 800; font-size: 31px; line-height: 33px; text-transform: uppercase;
  }
  .feature__note { font-size: 21px; line-height: 24px; text-transform: uppercase; }
  .feature { margin-bottom: 26px; }
  .feature--solo { margin-bottom: 28px; }
  .weight {
    position: absolute; left: 468px; top: 1112px; color: var(--cream);
    font-weight: 800; font-size: 40px; line-height: 1; text-transform: uppercase;
  }
  .weight small { font-size: 30px; }
</style>
</head>
<body>
  <main class="bag">
    <div class="bag__top-band"></div>

    <div class="brand">EMBERDEPOT.COM</div>

    <div class="rule rule--upper"></div>
    <h1 class="product-name product-name__first">BLAZEWOOD</h1>
    <div class="product-name product-name__second">CHARCOAL</div>
    <div class="rule rule--lower"></div>

    <div class="tagline">HI HEAT, LOW ASH, LONG BURNING</div>

    <div class="smoke-art" role="img" aria-label="Rising wisps of smoke"></div>
    <div class="flame-art" role="img" aria-label="Red flames rising from the bottom corner"></div>

    <section class="features">
      <div class="feature">
        <p class="feature__head">100% Natural Hardwood<br>Lump Charcoal</p>
        <p class="feature__note">No additives, no fillers</p>
      </div>
      <div class="feature">
        <p class="feature__head">Restaurant and<br>Competition Grade</p>
      </div>
      <div class="feature feature--solo">
        <p class="feature__note">Non sparking</p>
      </div>
      <div class="feature">
        <p class="feature__head">Easy Lighting</p>
        <p class="feature__note">Use a chimney starter</p>
        <p class="feature__note" style="margin-top:22px">Mild flavor profile</p>
      </div>
    </section>

    <div class="weight">22 <small>LBS</small>/10 <small>KG</small></div>
  </main>
</body>
</html>
```